Brindle Chill Supplies Stationery Design

Stationery Design

Thank you to all those who have submitted the logos. We have selected the logo for our new identity and we are now looking for stationery ideas.

The attached logo must be used in all stationery designs.

We require the following items of stationery:

1. Business Cards for 10 employees – Double Sided – All the card will have the same address:

7 – 31 Marrowby Lane, Kingston Upon Thames, Surrey, KT4 9QX, United Kingdom

Office phone number: +44 (0)208 613 7742

Freephone: 0800 129 4837

Fax: +44 (0)20 8731 2964

Website: www.brindlechill.example

The names on the cards and mobile numbers – will be given on selection of final design.

A few of the cards will have different emails but 5/6 card will have the same email address.

2. Letterhead A4 – same contact details as above – email address to be used info@brindlechill.example

3. Compliments Slip – same details as no.2

4. Envelope designs – with just the address, Freephone and Website.

Sizes Required: C4 – 324mm x 229mm – Windows and Regular

DL – 110mm x 220mm – Windows and Regular

5. A4 Ring Binder – Logo at the front and back and side; company name on the front and side of the binder (Brindle Chill Supplies); contact details at the back; same as number 2 above.

The ring binder will have food, drink and hygiene inserts inside and will act as a temporary brochure.

It may help with the design process to know we sell a range of frozen food products including chips, burgers, fish, frozen poultry items, vegetables, ice cream, desserts, bakery products, pies, pasties, onion rings, pizza toppings etc.

We also sell ambient products such as sauces, crisps such as dunmores, chocolates such as Hollensby, Vorelle, Quib etc.

Drinks wise we sell branded products such as zesta tonic, fizmo, lumra, glint, sky hare etc; As well as juices and mineral water.

We also sell hygiene products such as tissue paper, hand towels, and other washroom products, bleaches etc.

Our website doesn’t have the full range of products but gives you a good idea of what we do www.brindlechill.example

Please note we are looking for a classy, slick design so don’t worry about trying to add all the products on the binder design; these have just been given to assist with the design process.

We may add a slogan to the stationery but the final decision on this still has to be taken and the profile will be updated within the next 72 hours.

This project will only last a maximum of 10-14 days, we don’t want to drag it out like the logo so please only submit creative ideas; which have been given thought in terms of design, text and graphics.

Any questions, feel free to ask.

Thank you and we look forward to your designs.

Regards

Torvin Ashcombe

I've uploaded an Adobe Illustrator CS2.ai file, and an EPS file of my new logo so you can get better clarity within your designs for this project

Thanks
Torvin

Hi

We have had various questions in respect of dimensions and budget; we have addressed both issues below by providing dimensions and we will be increasing the budget to $500 as soon as Pixel Bazaar let us know how we can increase; they have already been emailed.

In respect of the dimensions, we have had various answers but here are the most common sizes.

 

There are various sizes of lever arch A4 folders but the most common ones are below:

 

 

• Dimensions width 28.5cm, height 32cm,spine 9cm
• Dimensions (mm)H:315 x W:285
• Dimensions (mm) H:31cm x W:27cm

 

The most common thickness in the UK seems to be 70mm; so can we use this as a guide please.

 

 

Compliment Slip Sizes:

 

• Our Compliment Slips are DL in size. You should design your Compliment Slip to DL dimension but also add a 3mm bleed around each edge.

 

Trim Size – 99mm x 210mm

 

With Bleed – 105mm – 216mm

 

 

Business Cards:

 

Trim Size: 85mm x 55mm

 

With Bleed: 91mm x 61mm

 

 

We have extended the time frame and the budget on this so look forward to new designs.

 

I hope this helps and all the best for Christmas and 2010..

 

Regards

Torvin Ashcombe.

Hi Guys

Another important point to mention as each country has different rules...

In the Uk the postage stamps go in the top right hand corner of the envelope so we will have to have our logo company details etc in either the top left or the bottom of the envelope.

Also all envelopes must have at the back our return address:

Return Address:

Brindle Chill Supplies Ltd
7 - 31 Marrowby Lane
Kingston Upon Thames
Surrey
KT4 9QX

So we could even have the business logo, name and website address at the front and the address at the back.

Regards

Torvin

```html
<!DOCTYPE html>
<html lang="en">
<head>
<meta charset="utf-8">
<title>Brindle Chill Supplies – Stationery</title>
<link rel="stylesheet" href="https://fonts.googleapis.com/css2?family=Source+Sans+3:wght@400;600&display=swap">
<style>
  :root {
    --ink-navy: #2b2a78;
    --ink-red: #b3262c;
    --ink-black: #141414;
    --rule: #3a3a3a;
    --paper: #ffffff;
    --mark: #2e3a86;
  }
  html, body {
    margin: 0;
    padding: 0;
    width: 1200px;
    height: 847px;
    overflow: hidden;
    background: var(--paper);
  }
  .sheet {
    position: relative;
    width: 1200px;
    height: 847px;
    font-family: "Source Sans 3", "Myriad Pro", Arial, sans-serif;
    color: var(--ink-navy);
  }
  .item {
    position: absolute;
    box-sizing: border-box;
    border: 1px solid var(--rule);
    background: var(--paper);
  }
  .flap {
    position: absolute;
    left: 0;
    top: 0;
    overflow: visible;
  }
  .flap polyline {
    fill: none;
    stroke: var(--rule);
    stroke-width: 1;
  }
  .return-address {
    position: absolute;
    left: 0;
    right: 0;
    margin: 0;
    text-align: center;
    font-size: 15px;
    line-height: 19px;
    color: var(--ink-navy);
  }

  /* brand lockup: plain circle + company name */
  .brand {
    position: absolute;
    display: flex;
    align-items: center;
  }
  .brand__dot {
    flex: none;
    border-radius: 50%;
    background: var(--mark);
  }
  .brand__name {
    font-weight: 600;
    color: var(--ink-black);
    line-height: 1;
    letter-spacing: 0.2px;
  }

  /* C4 envelope back */
  .envelope-c4 { left: 0; top: 0; width: 598px; height: 847px; }
  .envelope-c4 .return-address { top: 27px; }
  .envelope-c4 .brand { left: 0; right: 0; top: 736px; justify-content: center; gap: 14px; }
  .envelope-c4 .brand__dot { width: 62px; height: 62px; }
  .envelope-c4 .brand__name { font-size: 31px; }
  .envelope-c4 .web { position: absolute; left: 0; right: 0; top: 814px; margin: 0; text-align: center; font-size: 10px; color: var(--ink-black); }

  /* DL envelope back */
  .envelope-dl { left: 626px; top: 0; width: 574px; height: 288px; }
  .envelope-dl .return-address { top: 6px; }
  .envelope-dl .brand { left: 0; right: 0; top: 222px; justify-content: center; gap: 10px; }
  .envelope-dl .brand__dot { width: 48px; height: 48px; }
  .envelope-dl .brand__name { font-size: 23px; }

  /* business cards */
  .card { top: 348px; width: 233px; height: 134px; }
  .card--front { left: 673px; }
  .card--back { left: 933px; }

  .card--front .brand { left: 10px; top: 14px; gap: 10px; }
  .card--front .brand__dot { width: 52px; height: 52px; }
  .card--front .brand__name { font-size: 22px; line-height: 1.05; }
  .card__contact-name {
    position: absolute;
    left: 0; right: 0; top: 92px;
    margin: 0;
    text-align: center;
    font-size: 16px;
    font-variant: small-caps;
    color: var(--ink-red);
  }

  .card--back .brand { left: 8px; top: 8px; gap: 5px; }
  .card--back .brand__dot { width: 22px; height: 22px; }
  .card--back .brand__name { font-size: 10px; line-height: 1.1; }
  .card__address {
    position: absolute;
    right: 8px; top: 4px;
    margin: 0;
    text-align: right;
    font-size: 8.5px;
    line-height: 11px;
    color: var(--ink-navy);
  }
  .card__phones {
    position: absolute;
    left: 0; right: 0; top: 55px;
    margin: 0;
    text-align: center;
    font-size: 8.5px;
    line-height: 11px;
    color: var(--ink-navy);
  }
  .card__phones .label, .card__footer .label { color: var(--ink-red); }
  .card__footer {
    position: absolute;
    left: 5px; right: 5px; top: 114px;
    display: flex;
    justify-content: space-between;
    font-size: 8.5px;
    color: var(--ink-navy);
  }
</style>
</head>
<body>
<main class="sheet">

  <section class="item envelope-c4" aria-label="C4 envelope, back">
    <svg class="flap" width="598" height="120" viewBox="0 0 598 120" aria-hidden="true">
      <polyline points="0,0 66,118 530,118 598,0"/>
    </svg>
    <p class="return-address">7 - 31 Marrowby Lane,<br>Kingston Upon Thames,<br>Surrey, KT4 9QX</p>
    <div class="brand">
      <span class="brand__dot"></span>
      <span class="brand__name">Brindle Chill Supplies</span>
    </div>
    <p class="web">www.brindlechill.example</p>
  </section>

  <section class="item envelope-dl" aria-label="DL envelope, back">
    <svg class="flap" width="574" height="74" viewBox="0 0 574 74" aria-hidden="true">
      <polyline points="0,0 54,72 518,72 574,0"/>
    </svg>
    <p class="return-address">7 - 31 Marrowby Lane,<br>Kingston Upon Thames,<br>Surrey, KT4 9QX</p>
    <div class="brand">
      <span class="brand__dot"></span>
      <span class="brand__name">Brindle Chill Supplies</span>
    </div>
  </section>

  <section class="item card card--front" aria-label="Business card, front">
    <div class="brand">
      <span class="brand__dot"></span>
      <span class="brand__name">Brindle Chill<br>Supplies</span>
    </div>
    <p class="card__contact-name">Contact Name</p>
  </section>

  <section class="item card card--back" aria-label="Business card, back">
    <div class="brand">
      <span class="brand__dot"></span>
      <span class="brand__name">Brindle Chill<br>Supplies</span>
    </div>
    <p class="card__address">7 - 31 Marrowby Lane,<br>Kingston Upon Thames,<br>Surrey, KT4 9QX</p>
    <p class="card__phones">
      <span class="label">Office Phone:</span> +44 (0)208 613 7742<br>
      <span class="label">FreePhone:</span> 0800 129 4837<br>
      <span class="label">Fax:</span> +44 (0)20 8731 2964
    </p>
    <div class="card__footer">
      <span>www.brindlechill.example</span>
      <span><span class="label">email:</span> info@brindlechill.example</span>
    </div>
  </section>

</main>
</body>
</html>
```